Beekeeping company in need of a new attractive, simple website

We need a simple website for our Company 'Tarnfield Hives LLC' that will feature a couple different products that we offer (2019 NUCS & 2019 Queens) with the ability for customers to place orders for those products. Products will be for pickup only on specific dates so no shipping is required but will need dropdown menus to select which dates with limited quantities each date. Payments can be made through Paypal, Wix, and Square. Need the to ability to add and remove products from view on the site while maintaining information. Would like the ability to build a mailing list of potential customers and also connect visitors to our social media sites.
Beekeepers,

```html
<!DOCTYPE html>
<html lang="en">
<head>
<meta charset="utf-8">
<title>Tarnfield Hives LLC</title>
<link href="https://fonts.googleapis.com/css2?family=Lora:wght@700&family=Roboto:wght@400;500;700&display=swap" rel="stylesheet">
<style>
:root{
  --orange:#d9801c;
  --orange-deep:#c86f10;
  --amber:#e49a2c;
  --dark:#1b1b1b;
  --darker:#141414;
  --white:#ffffff;
  --muted:#cfcfcf;
  --social-a:#3b5494;
  --social-b1:#d6246e;
  --social-b2:#f1862c;
  --social-c:#1da1e4;
  --social-d:#e1322c;
}
*{margin:0;padding:0;box-sizing:border-box}
html,body{width:1200px;height:3689px;overflow:hidden}
body{position:relative;background:var(--dark);font-family:'Roboto',Arial,sans-serif;color:var(--white)}
.abs{position:absolute}
.serif{font-family:'Lora',Georgia,serif;font-weight:700}
.topbar{left:0;top:0;width:1200px;height:42px;background:var(--orange);text-align:center;font-size:15px;font-weight:700;line-height:42px;letter-spacing:1px}
.header{left:0;top:42px;width:1200px;height:110px;background:var(--darker)}
.brand-small{left:44px;top:40px;width:110px;text-align:center;font-family:'Lora',Georgia,serif;font-weight:700;font-size:17px;line-height:20px;color:var(--orange)}
.nav{left:0;top:46px;font-size:14px;font-weight:700;letter-spacing:.5px}
.nav span{position:absolute;top:0;white-space:nowrap}
.nav .active{color:var(--orange)}
.callus{left:824px;top:42px;font-size:20px;font-weight:700;color:var(--amber);white-space:nowrap}
.cart{left:1124px;top:28px}
.hero{left:0;top:152px;width:1200px;height:556px;background:radial-gradient(ellipse at 30% 50%,#8a5a22 0%,#5b3a18 45%,#2c1f12 100%)}
.hero-brand{left:90px;top:300px;width:450px;text-align:center;font-family:'Lora',Georgia,serif;font-weight:700;font-size:64px;line-height:74px;color:var(--white)}
.hero-brand .mark{display:block;width:60px;height:60px;border-radius:50%;background:var(--white);margin:0 auto 22px}
.newsletter{left:767px;top:256px;width:320px}
.newsletter .head{height:56px;background:var(--orange);text-align:center;font-size:22px;font-weight:700;line-height:56px}
.newsletter .body{background:var(--darker);padding:14px 24px 0;height:230px;clip-path:polygon(0 0,100% 0,100% 78%,50% 100%,0 78%)}
.newsletter label{display:block;font-size:15px;font-weight:700;margin-top:10px;margin-bottom:8px}
.field{height:38px;background:var(--white);color:#888;font-size:13px;line-height:38px;padding-left:14px}
.nl-btn{display:block;width:132px;height:40px;margin:30px auto 0;background:var(--orange);font-size:15px;font-weight:700;text-align:center;line-height:40px}
.h2{font-family:'Lora',Georgia,serif;font-weight:700;font-size:44px;text-align:center;width:1200px;left:0}
.photo{border:0}
.ptitle{font-family:'Lora',Georgia,serif;font-weight:700;font-size:38px}
.para{font-size:14px;line-height:32px;color:var(--white)}
.btn{background:var(--orange);font-size:14px;font-weight:700;text-align:center;color:var(--white)}
.btn-outline{border:2px solid var(--white);font-size:14px;font-weight:700;text-align:center}
.orange-sec{left:0;top:1780px;width:1200px;height:851px;background:linear-gradient(180deg,var(--orange) 0%,var(--amber) 55%,var(--orange-deep) 100%)}
.tile{top:2877px;height:202px}
.arrow{top:2960px}
.social{left:0;top:3214px;width:1200px;height:69px;display:flex}
.social div{flex:1;text-align:center;font-size:24px;font-weight:700;line-height:69px;letter-spacing:.5px}
.footer{left:0;top:3283px;width:1200px;height:406px;background:var(--darker)}
.fh{font-size:17px;font-weight:700;top:3380px;white-space:nowrap}
.flist{top:3424px;font-size:14px;line-height:28px}
.flist div::before{content:"»";margin-right:14px}
.fc{font-size:14px;line-height:22px}
.rule{left:111px;top:3607px;width:976px;height:1px;background:#444}
.copy{left:111px;top:3640px;font-size:13px}
.cards{left:890px;top:3640px;display:flex;gap:4px}
.cards span{width:34px;height:22px;border-radius:3px;background:#d8d8d8}
</style>
</head>
<body>

<div class="abs topbar">FREE SHIPPING ON YOUR EVERY ORDERS</div>

<header class="abs header"></header>
<div class="abs brand-small">Tarnfield<br>Hives LLC</div>
<nav class="abs nav" style="top:88px">
  <span class="active" style="left:197px">HOME</span>
  <span style="left:275px">PRODUCTS</span>
  <span style="left:393px">SERVICES</span>
  <span style="left:504px">ABOUT US</span>
  <span style="left:615px">CONTACT US</span>
</nav>
<div class="abs callus" style="top:84px">
  <svg width="18" height="18" viewBox="0 0 24 24" style="vertical-align:-2px;margin-right:10px"><path fill="var(--amber)" d="M6.6 10.8a15 15 0 006.6 6.6l2.2-2.2c.3-.3.7-.4 1-.2 1.1.4 2.3.6 3.6.6.6 0 1 .4 1 1V20c0 .6-.4 1-1 1A17 17 0 013 4c0-.6.4-1 1-1h3.5c.6 0 1 .4 1 1 0 1.3.2 2.5.6 3.6.1.3 0 .7-.2 1z"/></svg>Call us on : 555 010 2847
</div>
<svg class="abs cart" width="36" height="64" viewBox="0 0 36 64" style="top:62px">
  <circle cx="18" cy="12" r="10" fill="var(--amber)"/>
  <text x="18" y="16" text-anchor="middle" font-size="11" font-family="Roboto,sans-serif" font-weight="700" fill="#1b1b1b">0</text>
  <rect x="4" y="34" width="28" height="24" fill="none" stroke="#fff" stroke-width="2"/>
  <path d="M10 34v-5h16v5" fill="none" stroke="#fff" stroke-width="2"/>
  <line x1="10" y1="44" x2="26" y2="44" stroke="#fff" stroke-width="2"/>
</svg>

<section class="abs hero" role="img" aria-label="Close-up photograph of honey bees crawling over hive frames"></section>
<div class="abs hero-brand"><span class="mark"></span>Tarnfield<br>Hives LLC</div>

<form class="abs newsletter">
  <div class="head">JOIN THE NEWSLETTER</div>
  <div class="body">
    <label>NAME:</label>
    <div class="field">Enter Name</div>
    <label>EMAIL:</label>
    <div class="field">Enter Email</div>
    <span class="nl-btn">SUBSCRIBE</span>
  </div>
</form>

<h2 class="abs h2" style="top:820px">OUR PRODUCTS</h2>

<div class="abs ptitle" style="left:212px;top:1018px;width:300px;text-align:right">2019 NUCS</div>
<p class="abs para" style="left:112px;top:1098px;width:400px;text-align:right">Duis aute irure dolor in reprehenderit in voluptate velit esse cillum dolore eu fugiat nulla pariatur. Excepteur sint occaecat cupidatat non proident sunt in culpa qui</p>
<div class="abs btn" style="left:349px;top:1225px;width:160px;height:49px;line-height:49px">SHOP NOW ➜</div>
<div class="abs photo" role="img" aria-label="Photograph of bees clustered on a wooden nuc box" style="left:602px;top:954px;width:488px;height:416px;background:linear-gradient(135deg,#b8701e,#6b3e12 60%,#3a220c)"></div>

<div class="abs photo" role="img" aria-label="Photograph of bees at the entrance of orange hive boxes" style="left:199px;top:1372px;width:403px;height:416px;background:linear-gradient(90deg,#5c4a3a,#a8651c 60%,#e08a22)"></div>
<div class="abs photo" role="img" aria-label="Photograph of a single bee in flight" style="left:111px;top:1431px;width:302px;height:298px;background:radial-gradient(circle at 40% 55%,#d08c36,#8a6a4c 55%,#4a4038)"></div>
<div class="abs ptitle" style="left:688px;top:1448px">2019 QUEENS</div>
<p class="abs para" style="left:688px;top:1524px;width:410px">Duis aute irure dolor in reprehenderit in voluptate velit esse cillum dolore eu fugiat nulla pariatur. Excepteur sint occaecat cupidatat non proident sunt in culpa qui</p>
<div class="abs btn" style="left:688px;top:1652px;width:163px;height:50px;line-height:50px">SHOP NOW ➜</div>

<section class="abs orange-sec" role="img" aria-label="Soft background photograph of a bee on a flower"></section>
<svg class="abs" style="left:0;top:1779px" width="1200" height="200" viewBox="0 0 1200 200">
  <path d="M0 0H1200V30Q600 270 0 30Z" fill="var(--dark)"/>
</svg>

<h2 class="abs h2" style="top:2042px">BEEKEEPERS</h2>
<p class="abs para" style="left:200px;top:2122px;width:800px;text-align:center;line-height:30px">Duis aute irure dolor in reprehenderit in voluptate velit esse cillum dolore eu fugiat nulla pariatur. Excepteur cupidatat non proident, sunt in culpa qui officia deserunt mollit anim id est laborum.</p>
<div class="abs" role="img" aria-label="Photograph of beekeepers in protective suits tending hive boxes in an orchard" style="left:111px;top:2220px;width:477px;height:296px;border:4px solid #fff;background:linear-gradient(180deg,#6e8a3a,#4d6a2c 50%,#a6622a)"></div>
<div class="abs" style="left:661px;top:2200px;width:440px;font-family:'Lora',Georgia,serif;font-weight:700;font-size:34px;line-height:46px;letter-spacing:.5px">We Selling Bees To Other Beekeepers</div>
<p class="abs para" style="left:661px;top:2318px;width:430px;line-height:26px">Lorem ipsum dolor sit amet, consectetur adipiscing elit, sed do eiusmod tempor incididunt ut labore et dolore magna aliqua. Ut enim ad minim veniam, quis nostrud exercitation ullamco laboris nisi ut aliquip ex ea commodo consequat.</p>
<div class="abs btn-outline" style="left:661px;top:2464px;width:190px;height:42px;line-height:38px">REQUEST A QUOTE ➜</div>

<h2 class="abs h2" style="top:2755px">SNAPGRAM FEED</h2>
<div class="abs tile" role="img" aria-label="Photograph of bees packed on honeycomb" style="left:111px;width:228px;background:linear-gradient(135deg,#8a5a2a,#4a3020)"></div>
<div class="abs tile" style="left:364px;width:226px;background:var(--orange);padding:24px 20px;font-size:14px;line-height:22px">Lorem ipsum dolor temporset consectur <u>@loremipsum</u>
  <div style="position:absolute;left:0;bottom:38px;width:100%;text-align:center;font-size:15px">♥ 125 Likes</div>
</div>
<div class="abs tile" role="img" aria-label="Photograph of a bee on a purple flower" style="left:612px;width:227px;background:linear-gradient(135deg,#e0862a,#9a5a8a 65%,#4a3a6a)"></div>
<div class="abs tile" role="img" aria-label="Photograph of bees on a hive frame" style="left:861px;width:226px;background:linear-gradient(135deg,#6a4a2a,#b07828 55%,#3a2818)"></div>
<svg class="abs arrow" style="left:40px" width="20" height="36" viewBox="0 0 20 36"><path d="M16 4L4 18l12 14" fill="none" stroke="#fff" stroke-width="4"/></svg>
<svg class="abs arrow" style="left:1140px" width="20" height="36" viewBox="0 0 20 36"><path d="M4 4l12 14L4 32" fill="none" stroke="#fff" stroke-width="4"/></svg>

<div class="abs social">
  <div style="background:var(--social-a)">CIRCLEBOOK</div>
  <div style="background:linear-gradient(90deg,var(--social-b1),var(--social-b2))">SNAPGRAM</div>
  <div style="background:var(--social-c)">CHIRPER</div>
  <div style="background:var(--social-d)">PINWALL</div>
</div>

<footer class="abs footer"></footer>
<div class="abs fh" style="left:111px">QUICK LINKS</div>
<div class="abs fh" style="left:302px">SUPPORT</div>
<div class="abs fh" style="left:534px">CONTACT US</div>
<div class="abs fh" style="left:843px">NEWSLETTER SUBSCRIPTION</div>

<div class="abs flist" style="left:111px"><div>Home</div><div>About Us</div><div>Products</div><div>Honey Bees</div><div>Bekeepers</div></div>
<div class="abs flist" style="left:302px"><div>Shipping</div><div>Quantity</div><div>Payment Methods</div><div>Terms Of Services</div><div>Privacy Policy</div></div>

<svg class="abs" style="left:534px;top:3428px" width="14" height="18" viewBox="0 0 14 18"><path d="M7 0a7 7 0 00-7 7c0 5 7 11 7 11s7-6 7-11a7 7 0 00-7-7zm0 10a3 3 0 110-6 3 3 0 010 6z" fill="#fff"/></svg>
<div class="abs fc" style="left:562px;top:3424px;width:230px">48 Clover Lane, Meadow City,<br>State, ER. Po: 20417</div>
<svg class="abs" style="left:534px;top:3488px" width="14" height="14" viewBox="0 0 24 24"><path fill="#fff" d="M6.6 10.8a15 15 0 006.6 6.6l2.2-2.2c.3-.3.7-.4 1-.2 1.1.4 2.3.6 3.6.6.6 0 1 .4 1 1V20c0 .6-.4 1-1 1A17 17 0 013 4c0-.6.4-1 1-1h3.5c.6 0 1 .4 1 1 0 1.3.2 2.5.6 3.6.1.3 0 .7-.2 1z"/></svg>
<div class="abs fc" style="left:562px;top:3484px">(+1) 555 014 7720</div>
<svg class="abs" style="left:534px;top:3530px" width="16" height="12" viewBox="0 0 16 12"><rect width="16" height="12" fill="#fff"/><path d="M0 0l8 6 8-6" fill="none" stroke="#141414" stroke-width="1.5"/></svg>
<div class="abs fc" style="left:562px;top:3525px">sales@tarnfieldhives.com</div>

<div class="abs" style="left:843px;top:3421px;width:240px;font-size:12px;line-height:20px">Register your Email Address to get more Information about us</div>
<div class="abs" style="left:843px;top:3472px;width:244px;height:32px;background:#fff;color:#888;font-size:12px;line-height:32px;padding-left:10px">Email Address</div>
<div class="abs btn" style="left:843px;top:3520px;width:113px;height:36px;line-height:36px;font-size:13px">SUBSCRIBE</div>

<div class="abs rule"></div>
<div class="abs copy">© 2019 Tarnfield Hives LLC.  All Rights Reserved.</div>
<div class="abs cards"><span></span><span></span><span></span><span></span><span></span></div>

</body>
</html>
```